Velmora Outcomes Brochure Design Project

- Who we are?
Velmora Outcomes is New Internet Marketing Company Based in China.

It is our aim to provide Chinese clients with the means to internationally market their product, via the Internet.

Our primary products are Outsourced Design ( Thanks to Pixel hive and the amazing designers who use it), SEO and Virtual Hosting.

- Project Brief
Design a vibrant and fresh brochure that introduces the fundamentals of SEO. There is no restriction to the number of pages, however all the info I have included in this brief must be included.

- Colour Palette
Please see link or download the Adobe Swatch Exchange File or follow the link below
http://tintaro.example.com/#themes/search?term=5830716
Updates

Logo updated - grey background removed

Various file formats added for logo and brochure content

Brochure zip file add containing logo in different formats.

Adobe color scheme file added

The general corporate colors are:

Base Color: CMYK :0, 60, 80, 0  Hex: FF6633
Dark Orange: CMYK: 0, 72, 96, 30 Hex: B23308
Light Orange: CMYK 0, 42, 56, 0 Hex: FF9571
Grey: CMYK 0, 0, 0, 48 Hex: 858585
Light Grey: CMYK 0, 0, 0, 26 Hex: BDBDBD

Please note that I'm happy for other colors to be included, however I would like these the corporate branding colors to be clearly present through the brochure.

Hi All

First place payment has increased to $600 - Looking to see some creative designs!

Hi All

Project Deadline Extended
Reason: I have increase the budget and extend the deadline as I need to see more design.

I have attached a zip file that contains example brochures I like.

We are not keen on the table data its a little plain. We have create an info-graphic to replace one of the table and would like to see it included in the design.

Project Deadline Extended
Reason: A few designers have asked for this extension and I would like to see additional designs. Thanks Marek

Target Market(s)

- Our Target Audience is..
It is small to medium businesses looking to reach out to the international market.
Our clients still very much operate on a face to face level in business and are new to the concept of Internet marketing

However this must look professional, Marketable and Clean, with the power of connecting people globally, through SEO and design to be reflected visually in the brochure.

Industry/Entity Type

Internet

Requirements
Must have
• One or more of the FACTS that I have highlighted need to stand out on each page. These FACTS can be found the document attached to this brief and are under the section titled 'Did You Know!'. Not every fact in this section needs to be highlighted in the brochure, but each page needs to have at least, one or more fact that stands out, soemwhere on the page.
See attached document, under the heading 'Did you Know!' and use one or two of these facts to spruce up the pages!

One image/ per page or per two pages MUST be included!

- Provide stock photos and please send us a message with the additional cost of these with your submission

The Table data, that I have included in the attachment must be included in the body of the pages - BUT the table format is not necessary and you can place the information in the body like plain text.

The brochure size should be a little larger than A4.

Please design the back page, like a pocket to hold paper and other material in it that I include with this brochure.

```html
<!DOCTYPE html>
<html lang="en">
<head>
<meta charset="utf-8">
<title>Velmora Outcomes – Brochure proposal</title>
<link href="https://fonts.googleapis.com/css2?family=Open+Sans:wght@300;400;600;700;800&display=swap" rel="stylesheet">
<style>
:root{
  --orange:#f26522;
  --orange-deep:#d9541c;
  --orange-dark:#b23308;
  --orange-light:#ff9571;
  --grey:#858585;
  --grey-light:#bdbdbd;
  --charcoal:#3b3939;
  --paper:#ffffff;
  --board:#e9e9e9;
  --ink:#555555;
}
*{margin:0;padding:0;box-sizing:border-box}
html,body{width:1000px;height:1200px;overflow:hidden}
body{
  position:relative;
  background:radial-gradient(ellipse at 50% 40%,#f4f4f4 0%,var(--board) 70%,#dedede 100%);
  font-family:"Open Sans",Arial,sans-serif;color:var(--ink);
}
.spread{position:absolute;width:420px;height:148px;display:flex;box-shadow:0 3px 6px rgba(0,0,0,.25)}
.col-left{left:52px}.col-right{left:482px}
.row-1{top:104px}.row-2{top:265px}.row-3{top:421px}.row-4{top:579px}.row-5{top:734px}.row-6{top:890px}
.page{position:relative;width:210px;height:148px;background:var(--paper);overflow:hidden}
.page.dark{background:var(--charcoal)}
.page.orange{background:var(--orange-deep)}
.page.soft{background:#f3f3f3}
.block{position:absolute}
.tiny{font-size:3.3px;line-height:4.1px;color:var(--ink);text-align:justify}
.dark .tiny{color:#d8d8d8}
.tiny h4{font-size:3.9px;line-height:4.8px;color:var(--orange);font-weight:700;margin-bottom:.6px;text-align:left}
.dark .tiny h4.light{color:#fff}
.tiny p{margin-bottom:1.6px}
.fact{color:var(--orange);font-weight:700}
.brand{display:flex;align-items:center;gap:3px;font-weight:700;white-space:nowrap}
.brand .dot{border-radius:50%;border:1.2px solid currentColor;flex:none}
.brand-white{color:#fff}
.brand-orange{color:var(--orange)}
.brand-grey{color:#a8a8a8}
.brand-faint{color:#d6d6d6}
.tagline{color:#fff;font-weight:400}
.band-grey{position:absolute;background:var(--grey-light)}
.label-bar{position:absolute;background:var(--orange);color:#fff;font-size:3.6px;line-height:6px;padding:0 4px;white-space:nowrap}
.chart{position:absolute}
.photo{position:absolute}
.rate{position:absolute;font-size:3px;line-height:3.7px;color:var(--ink);border-collapse:collapse}
.rate th{font-weight:700;text-align:left;color:#333;padding-right:6px}
.rate td{padding-right:6px;white-space:nowrap}
.list{font-size:3.2px;line-height:4px;color:var(--ink)}
.caption{font-size:6px;color:#555;position:absolute}
.blog-band{position:absolute;left:0;top:0;width:100%;height:44px;background:var(--charcoal)}
.blog-word{position:absolute;left:8px;top:14px;font-size:26px;font-weight:800;color:var(--orange);letter-spacing:-1px}
.logo-card{position:absolute;background:#fff;box-shadow:0 1px 3px rgba(0,0,0,.2);display:flex;align-items:center;justify-content:center}
.logo-name{font-weight:700;font-size:6.5px;color:#444;display:flex;align-items:center;gap:3px}
.logo-name .sq{width:6px;height:6px;background:var(--orange);flex:none}
.cover{position:absolute;left:540px;top:770px;width:380px;height:262px;box-shadow:0 6px 14px rgba(0,0,0,.3);background:var(--orange-deep);overflow:hidden}
.cover-top{position:absolute;left:0;top:0;width:250px;height:118px;background:#a8441b}
.cover-grey{position:absolute;left:250px;top:0;width:130px;height:118px;background:var(--grey)}
.cover-title{position:absolute;left:150px;top:175px;font-size:16px;color:#fff;font-weight:400}
.proposal-title{position:absolute;left:750px;top:1128px;font-size:22px;font-weight:300;color:#555}
</style>
</head>
<body>

<svg width="0" height="0" style="position:absolute" aria-hidden="true">
  <defs>
    <symbol id="process-chart" viewBox="0 0 100 100">
      <circle cx="50" cy="50" r="44" fill="none" stroke="#bdbdbd" stroke-width="0.6"/>
      <circle cx="50" cy="50" r="12" fill="none" stroke="#bdbdbd" stroke-width="0.6"/>
      <g stroke="#f26522" stroke-width="6">
        <line x1="63" y1="50" x2="90" y2="50" transform="rotate(-150 50 50)"/>
        <line x1="63" y1="50" x2="84" y2="50" transform="rotate(-120 50 50)"/>
        <line x1="63" y1="50" x2="92" y2="50" transform="rotate(-90 50 50)"/>
        <line x1="63" y1="50" x2="80" y2="50" transform="rotate(-60 50 50)"/>
        <line x1="63" y1="50" x2="88" y2="50" transform="rotate(-30 50 50)"/>
        <line x1="63" y1="50" x2="78" y2="50" transform="rotate(0 50 50)"/>
        <line x1="63" y1="50" x2="86" y2="50" transform="rotate(30 50 50)"/>
        <line x1="63" y1="50" x2="82" y2="50" transform="rotate(60 50 50)"/>
      </g>
      <g stroke="#858585" stroke-width="6">
        <line x1="63" y1="50" x2="74" y2="50" transform="rotate(90 50 50)"/>
        <line x1="63" y1="50" x2="70" y2="50" transform="rotate(120 50 50)"/>
        <line x1="63" y1="50" x2="76" y2="50" transform="rotate(150 50 50)"/>
        <line x1="63" y1="50" x2="72" y2="50" transform="rotate(180 50 50)"/>
      </g>
      <g font-family="Open Sans, sans-serif" font-size="3.4" fill="#777">
        <text x="28" y="6">Design Brief</text>
        <text x="72" y="14">Concepts</text>
        <text x="86" y="44">Revisions</text>
        <text x="70" y="92">Final Files</text>
        <text x="4" y="82">Delivery</text>
      </g>
    </symbol>
  </defs>
</svg>

<!-- Spread 1: cover spread -->
<section class="spread col-left row-1">
  <div class="page orange">
    <div class="block" style="left:0;top:0;width:158px;height:74px;background:#c9501d"></div>
    <div class="block" style="left:158px;top:0;width:52px;height:74px;background:var(--grey)"></div>
    <div class="block brand brand-white" style="left:162px;top:34px;font-size:3.9px"><span class="dot" style="width:5px;height:5px"></span>VelmoraOutcomes.com</div>
    <div class="block tagline" style="left:92px;top:118px;font-size:7.5px">SEO and Cloud Consultant</div>
  </div>
  <div class="page dark">
    <div class="block brand brand-orange" style="left:60px;top:70px;font-size:8px"><span class="dot" style="width:10px;height:10px"></span>VelmoraOutcomes.com</div>
  </div>
</section>

<!-- Spread 2: logo process and SEO intro -->
<section class="spread col-left row-2">
  <div class="page dark">
    <div class="block tiny" style="left:5px;top:10px;width:44px">
      <h4>Logo Design</h4>
      <p>We guide each client through a clear brief, early sketches, revisions and final artwork ready for print and web use. Many designers work on one brief at once, so you see a wide choice of ideas.</p>
      <h4>Why choose our way?</h4>
      <p>A studio sends two or three ideas. Our method brings dozens of concepts from designers around the world, and you only pay for the one you pick. Every file is yours to use in print, on screen and on signs.</p>
    </div>
    <svg class="chart" style="left:52px;top:10px" width="92" height="92" role="img" aria-label="Radial chart of the logo design process"><use href="#process-chart"/></svg>
    <div class="block tiny" style="left:150px;top:10px;width:54px">
      <h4>The design process</h4>
      <p>1. Send us your brief and the look you like.</p>
      <p>2. Designers post first ideas within days.</p>
      <p>3. You rate each concept and leave notes.</p>
      <p>4. The best designers refine their work.</p>
      <p>5. You choose the winner and approve it.</p>
      <p>6. Final files arrive in every format.</p>
      <p>7. Compare this with the traditional agency method and its single designer.</p>
    </div>
    <div class="block tiny" style="left:5px;top:126px;width:150px">
      <h4 class="light">How long does it take?</h4>
      <p>Most logo projects close within ten to fourteen days, and we have seen happy clients choose in less than one week.</p>
    </div>
  </div>
  <div class="page">
    <div class="block brand brand-grey" style="right:6px;top:4px;font-size:3.6px">VelmoraOutcomes.com</div>
    <div class="block tiny" style="left:7px;top:14px;width:60px">
      <h4>SEO</h4>
      <p>Search engines decide who finds you. Good optimisation places your pages in front of buyers abroad, at the very moment they look for what you sell.</p>
      <h4>Why is it so important?</h4>
      <p>Most people never look past the first page of results, so ranking well brings steady new visitors without paying for each click.</p>
    </div>
    <div class="block tiny" style="left:74px;top:14px;width:60px">
      <h4>How do I get found?</h4>
      <p>People type short phrases into a search box. When your pages use those same words, and other sites link to you, engines trust you more and rank you higher.</p>
      <h4>SEO</h4>
      <p>We study your market, pick the right phrases and shape each page so it reads well for buyers and for search engines.</p>
    </div>
    <div class="block tiny" style="left:141px;top:14px;width:62px">
      <p>Results build month after month. Unlike an advert, a strong page keeps working long after the work is done.</p>
      <h4>Did you know?</h4>
      <p class="fact">Nine in ten searchers click a result on the first page.</p>
      <p>Three out of four users never scroll past the first page of results.</p>
    </div>
    <div class="band-grey" style="left:74px;top:96px;width:136px;height:30px"></div>
    <div class="block brand brand-faint" style="left:82px;top:108px;font-size:4px"><span class="dot" style="width:5px;height:5px"></span>VelmoraOutcomes.com</div>
  </div>
</section>

<!-- Spread 3: process chart and SEO packages -->
<section class="spread col-left row-3">
  <div class="page">
    <svg class="chart" style="left:30px;top:6px" width="136" height="136" role="img" aria-label="Radial chart of the logo design process"><use href="#process-chart"/></svg>
    <div class="label-bar" style="left:0;top:70px">Logo design - Our method Vs Traditional</div>
  </div>
  <div class="page">
    <div class="block brand brand-grey" style="left:8px;top:38px;font-size:5px"><span class="dot" style="width:6px;height:6px"></span>VelmoraOutcomes.com</div>
    <svg class="block" style="left:30px;top:4px" width="50" height="34" aria-hidden="true">
      <g fill="none" stroke="#cfcfcf" stroke-width="2">
        <path d="M8 34V12M3 17l5-5 5 5"/><path d="M25 34V6M20 11l5-5 5 5"/><path d="M42 34V2M37 7l5-5 5 5"/>
      </g>
    </svg>
    <div class="block tiny" style="left:94px;top:20px;width:58px">
      <h4>SEO Packages</h4>
      <p>Whether you are just starting out or run a well established business, we have an SEO package that fits your goals.</p>
      <p>All of our packages include the following site optimisation services, so your pages are ready to rank.</p>
    </div>
    <div class="block list" style="left:158px;top:20px;width:50px">Website Analysis<br>Competitor Analysis<br>Keyword Research<br>Title Optimisation<br>Meta Descriptions<br>Content Optimisation<br>Image Optimisation<br>Site Map Setup<br>Link Building<br>Analytics Setup<br>Monthly Report</div>
    <div class="band-grey" style="left:0;top:84px;width:210px;height:30px"></div>
    <div class="block tiny" style="left:8px;top:87px;width:76px">
      <h4>Our custom package</h4>
      <p>Every business is different. Tell us your goals and budget and we will build a plan around the keywords and markets that matter to you.</p>
    </div>
    <table class="rate" style="left:124px;top:88px">
      <tr><th>Website Size</th><th>10 pages</th></tr>
      <tr><td>No. of Keywords</td><td>5</td></tr>
      <tr><td>Keywords in Top 10</td><td>3</td></tr>
      <tr><td>Directory Submission</td><td>100</td></tr>
      <tr><td>Article Writing</td><td>2</td></tr>
      <tr><td>Social Bookmarking</td><td>50</td></tr>
      <tr><td>Press Release</td><td>1</td></tr>
      <tr><td>Blog Posting</td><td>4</td></tr>
      <tr><td>Monthly Report</td><td>Yes</td></tr>
    </table>
  </div>
</section>

<!-- Spread 4: packages and website design -->
<section class="spread col-left row-4">
  <div class="page">
    <div class="block tiny" style="left:7px;top:6px;width:96px"><h4>Small Business Silver Package</h4><p>Do you have a small business and are looking to reach buyers abroad? This plan covers the basics and gets your pages found.</p></div>
    <table class="rate" style="left:112px;top:6px">
      <tr><th>Website Size</th><th>10 pages</th></tr>
      <tr><td>No. of Keywords</td><td>5</td></tr>
      <tr><td>Keywords in Top 10</td><td>3</td></tr>
      <tr><td>Directory Submission</td><td>100</td></tr>
      <tr><td>Article Writing</td><td>2</td></tr>
      <tr><td>Monthly Report</td><td>Yes</td></tr>
    </table>
    <div class="block tiny" style="left:7px;top:46px;width:96px"><h4>Medium Business Gold Package</h4><p>A growing firm with a wider range of products needs more keywords, more content and steady link building every month.</p></div>
    <table class="rate" style="left:112px;top:46px">
      <tr><th>Website Size</th><th>25 pages</th></tr>
      <tr><td>No. of Keywords</td><td>10</td></tr>
      <tr><td>Keywords in Top 10</td><td>6</td></tr>
      <tr><td>Directory Submission</td><td>250</td></tr>
      <tr><td>Article Writing</td><td>4</td></tr>
      <tr><td>Monthly Report</td><td>Yes</td></tr>
    </table>
    <div class="block tiny" style="left:7px;top:86px;width:96px"><h4>Large Business Platinum Package</h4><p>For large sites selling in many countries, with full keyword research, content writing and a monthly review call.</p></div>
    <table class="rate" style="left:112px;top:86px">
      <tr><th>Website Size</th><th>50 pages</th></tr>
      <tr><td>No. of Keywords</td><td>20</td></tr>
      <tr><td>Keywords in Top 10</td><td>12</td></tr>
      <tr><td>Directory Submission</td><td>500</td></tr>
      <tr><td>Article Writing</td><td>8</td></tr>
      <tr><td>Monthly Report</td><td>Yes</td></tr>
    </table>
    <div class="block tiny" style="left:7px;top:132px;width:150px"><p>* Included in both the gold and platinum package is social media marketing.</p></div>
  </div>
  <div class="page dark">
    <div class="block tiny" style="left:6px;top:4px;width:198px"><h4 class="light">Website Design</h4><p>A well designed site is your shop window to the world. We build clean pages that load fast, read well on any screen and turn visitors from every market into buyers.</p></div>
    <div class="photo" style="left:8px;top:34px;width:112px;height:92px;background:linear-gradient(135deg,#2c2c2c,#4a4a4a)" role="img" aria-label="Photo of a hand sketching a website layout on a board"></div>
    <div class="block" style="left:124px;top:52px;width:86px;height:96px;background:#fff"></div>
    <div class="block tiny" style="left:127px;top:55px;width:39px"><h4>Why choose us?</h4><p>Competition is about ideas. You see many designs from many designers before you decide, and you pay only for the design you love. Our team guides you at every step.</p></div>
    <div class="block tiny" style="left:169px;top:55px;width:38px"><h4>The design process</h4><p>1. Send your brief.</p><p>2. Designers post ideas.</p><p>3. Rate and give notes.</p><p>4. Pick a winner.</p><p>5. We build the site and launch it for you.</p></div>
  </div>
</section>

<!-- Spread 5: cloud computing -->
<section class="spread col-left row-5">
  <div class="page">
    <svg class="chart" style="left:10px;top:2px" width="120" height="120" role="img" aria-label="Radial chart of the logo design process"><use href="#process-chart"/></svg>
    <div class="label-bar" style="left:0;top:70px;background:var(--grey)">Logo design - Our method Vs Traditional</div>
    <div class="block tiny" style="left:6px;top:126px;width:120px"><h4>How long does it take?</h4><p>Most logo projects close within ten to fourteen days.</p></div>
  </div>
  <div class="page">
    <div class="block tiny" style="left:7px;top:10px;width:58px"><h4>Cloud computing and international hosting</h4><p>Cloud hosting places your site on servers close to your buyers, so pages open fast in every country you sell to.</p><p>There is no hardware to buy and no server room to run. You pay for what you use and grow when you need.</p><h4>Local servers</h4><p>Host near your market and search engines see you as a local site.</p></div>
    <div class="block tiny" style="left:70px;top:10px;width:58px"><p>We set up, watch and update your hosting, so you can focus on your customers and your products.</p><p class="fact">Nine in ten searchers click a result on the first page.</p><p>Do you want to find out more? Talk to our team about a hosting plan that fits your needs and your budget.</p><p class="fact">Contact us about our international hosting service today!</p></div>
    <div class="photo" style="left:136px;top:6px;width:68px;height:136px;background:linear-gradient(180deg,#e4e4e4,#bfbfbf)" role="img" aria-label="Photo of logo sketches pinned to a wall"></div>
  </div>
</section>

<!-- Spread 6: blog -->
<section class="spread col-left row-6">
  <div class="page">
    <div class="blog-band"></div>
    <div class="blog-word">blog</div>
    <div class="block tiny" style="left:7px;top:50px;width:60px"><p>You may be asking why we have dedicated a whole page to blogging. The answer is simple: fresh posts give search engines new pages to find and give buyers a reason to come back.</p><p>Each post can target a new phrase your customers type, and every visit helps your whole site rank.</p><h4>What is this?</h4><p>A blog is a set of short articles on your site about your products, your trade and your news.</p></div>
    <div class="block tiny" style="left:73px;top:50px;width:60px"><p>Great posts are shared by readers, and each share brings new visitors and new links to your site.</p><p>We can write posts for you in clear English, plan a calendar of topics and place each one where it helps most.</p><p>Start with one post a week and you will soon see more pages indexed and more visitors arriving from search.</p></div>
  </div>
  <div class="page">
    <div class="block tiny" style="left:7px;top:8px;width:60px"><h4>Did you know that?</h4><p class="fact">Nine in ten searchers click a result on the first page.</p><p>Over half of all web traffic now comes from search engines, and most of it goes to the top three results.</p><p>Buyers abroad search in English first, so clear English pages open your products to the whole world.</p><p>Sites with a blog have far more pages indexed than sites without one.</p></div>
    <div class="block tiny" style="left:73px;top:8px;width:60px"><h4>Credits</h4><p>Most searchers trust organic results more than paid adverts.</p><p>Four out of five searchers ignore the sponsored links.</p><p>Seven in ten users click an organic link over an advert.</p><p>Local search brings buyers who are ready to act.</p><h4>Previous Results</h4><p>Halcyon Lamp, one of the largest makers of outdoor screens, chose its new logo from many concepts in under two weeks.</p></div>
  </div>
</section>

<!-- Right column: portfolio -->
<section class="spread col-right row-1">
  <div class="page soft">
    <div class="caption" style="left:12px;top:72px">Lunaris winner choice</div>
    <div class="photo" style="left:98px;top:10px;width:108px;height:128px;background:linear-gradient(180deg,#9b1c2a,#f0f0f0 60%)" role="img" aria-label="Screenshot of a client website with a red header"></div>
  </div>
  <div class="page soft">
    <div class="photo" style="left:8px;top:10px;width:194px;height:128px;background:linear-gradient(180deg,#a0165f,#d93b8a 55%,#2a2a2a 85%)" role="img" aria-label="Screenshot of a client website in magenta"></div>
  </div>
</section>

<section class="spread col-right row-2">
  <div class="page soft">
    <div class="photo" style="left:8px;top:8px;width:194px;height:132px;background:linear-gradient(180deg,#a0165f,#d93b8a 55%,#2a2a2a 85%)" role="img" aria-label="Screenshot of a client website in magenta"></div>
  </div>
  <div class="page soft">
    <div class="block tiny" style="left:8px;top:8px;width:120px"><p>Logo Design<br>Halcyon Lamp<br>Halcyon Lamp and the makers of some of the world's largest outdoor LED screens.</p></div>
    <div class="photo" style="left:8px;top:42px;width:196px;height:100px;background:linear-gradient(180deg,#1d2a4a,#3d5fa0 50%,#5a4630)" role="img" aria-label="Photo of a large outdoor LED screen in an arena"></div>
  </div>
</section>

<section class="spread col-right row-3">
  <div class="page soft">
    <div class="photo" style="left:40px;top:10px;width:130px;height:128px;background:linear-gradient(180deg,#1a1a1a,#2e2e2e 60%,#6a2b4a)" role="img" aria-label="Screenshot of a dark client website"></div>
  </div>
  <div class="page soft">
    <div class="block tiny" style="left:8px;top:8px;width:150px"><p>Halcyon Lamp chose its new logo from many concepts and was very happy with the final result. See the final choice below.</p></div>
    <div class="logo-card" style="left:12px;top:44px;width:86px;height:82px"><span class="logo-name"><span class="sq"></span>Halcyon Lamp</span></div>
    <div class="block" style="left:118px;top:32px;width:54px;height:100px;background:linear-gradient(180deg,#fff 0 34%,#2f5874 34% 67%,#3a3a3a 67%)"></div>
    <div class="block" style="left:124px;top:43px;font-size:4.5px;font-weight:700;color:#444">Halcyon Lamp</div>
    <div class="block" style="left:124px;top:76px;font-size:4.5px;font-weight:700;color:#fff">Halcyon Lamp</div>
    <div class="block" style="left:124px;top:109px;font-size:4.5px;font-weight:700;color:#fff">Halcyon Lamp</div>
  </div>
</section>

<section class="spread col-right row-4">
  <div class="page soft">
    <div class="logo-card" style="left:8px;top:28px;width:90px;height:90px"><span class="logo-name"><span class="sq"></span>Halcyon Lamp</span></div>
    <div class="logo-card" style="left:110px;top:28px;width:90px;height:90px"><span class="logo-name">Halcyon Lamp</span></div>
  </div>
  <div class="page soft">
    <div class="logo-card" style="left:8px;top:28px;width:90px;height:90px"><span class="logo-name"><span class="sq"></span>Halcyon Lamp</span></div>
    <div class="logo-card" style="left:110px;top:28px;width:90px;height:90px"><span class="logo-name" style="font-weight:400;font-size:7px">Halcyon Lamp</span></div>
  </div>
</section>

<!-- Front cover -->
<section class="cover">
  <div class="cover-top"></div>
  <div class="cover-grey"></div>
  <div class="block brand brand-white" style="left:262px;top:52px;font-size:8px"><span class="dot" style="width:10px;height:10px"></span>VelmoraOutcomes.com</div>
  <div class="cover-title">SEO and Cloud Consultant</div>
</section>

<div class="proposal-title">Brochure proposal</div>

</body>
</html>
```